Help keep hoosiers happy and at home!

We need a billboard designed for our Indiana based healthcare business called 'Willow Hearth Caregivers'. We administer a medicaid waiver program that provides support and financial aid to live in caregivers that take care of someone who would otherwise be in a nursing home or skilled nursing facility. Qualified caregivers could be eligible to receive up to 1200 dollars a month in tax free financial aid, as well as access to nursing support that helps manage any unexpected situations or changes in a care recipients condition or care routine. Our program empowers families to keep their loved ones at home and out of the nursing home. NOTE: We believe the tagline at the bottom of our logo is disproportionately small. We would like to see that tagline larger and easier to read. I look forward to seeing your design ideas!

Target Market(s)

Medicaid aged beneficiaries and caregivers.

Industry/Entity Type

Home Healthcare

Colors
0054AA
0677BA
7BADD7
CADEEF
E8F1F8

Requirements
Nice to have
• "Empowering friends and family to care for their loves ones at home. Eligible participants receive up to $15,000 a year, tax free."

```html
<!DOCTYPE html>
<html lang="en">
<head>
<meta charset="UTF-8">
<title>Willow Hearth Caregivers Billboard</title>
<link rel="stylesheet" href="https://fonts.googleapis.com/css2?family=Poppins:wght@400;600;800&display=swap">
<style>
  :root {
    --page: #ffffff;
    --navy-light: #2156a6;
    --navy-mid: #223f86;
    --navy-deep: #1b2558;
    --brand-blue: #0677ba;
    --bright-cyan: #00b4ec;
    --ring-blue: #1f3b78;
    --photo-top: #0f6fbf;
    --photo-bottom: #2d4f90;
    --white: #ffffff;
  }
  * { margin: 0; padding: 0; box-sizing: border-box; }
  html, body {
    width: 1200px; height: 1000px; overflow: hidden;
    background: var(--page);
    font-family: "Poppins", sans-serif;
  }
  .billboard {
    position: absolute;
    left: 153px; top: 314px;
    width: 895px; height: 371px;
    overflow: hidden;
    background: linear-gradient(110deg, var(--navy-light) 0%, var(--navy-mid) 45%, var(--navy-deep) 100%);
    color: var(--white);
  }
  .billboard-shapes { position: absolute; inset: 0; }
  .brand {
    position: absolute; left: 26px; top: 54px;
    display: flex; align-items: center; gap: 8px;
  }
  .brand-dot {
    width: 14px; height: 14px; border-radius: 50%;
    background: var(--white);
  }
  .brand-name {
    font-weight: 600; font-size: 15px; line-height: 1.15;
    color: var(--white); width: 120px;
  }
  .headline {
    position: absolute; left: 31px; top: 142px;
    font-weight: 800; font-size: 49px; line-height: 50px;
    letter-spacing: -1.2px; text-transform: uppercase;
  }
  .tagline-band {
    position: absolute; left: 0; top: 248px;
    width: 320px; height: 40px;
    background: var(--bright-cyan);
    clip-path: polygon(0 0, 100% 0, 97% 100%, 0 100%);
  }
  .tagline-text {
    position: absolute; left: 35px; top: 248px;
    font-weight: 800; font-size: 28px; line-height: 40px;
    letter-spacing: -0.5px; text-transform: uppercase;
  }
  .benefit {
    position: absolute; left: 30px; top: 299px;
    font-weight: 400; font-size: 17.5px; line-height: 22px;
  }
  .benefit strong { font-weight: 800; }
  .call {
    position: absolute; left: 385px; top: 287px;
    width: 210px; text-align: center;
  }
  .call-label { font-weight: 400; font-size: 17px; line-height: 22px; text-transform: uppercase; }
  .call-number { font-weight: 600; font-size: 26px; line-height: 34px; letter-spacing: -0.3px; }
</style>
</head>
<body>
  <section class="billboard">
    <svg class="billboard-shapes" width="895" height="371" viewBox="0 0 895 371">
      <defs>
        <linearGradient id="photoFill" x1="0" y1="0" x2="0" y2="1">
          <stop offset="0" stop-color="var(--photo-top)"/>
          <stop offset="1" stop-color="var(--photo-bottom)"/>
        </linearGradient>
      </defs>
      <!-- corner circle behind brand -->
      <circle cx="93" cy="-22" r="147" fill="var(--brand-blue)" opacity="0.75"/>
      <circle cx="93" cy="-22" r="153" fill="none" stroke="var(--white)" stroke-width="1"/>
      <!-- top right circle -->
      <circle cx="851" cy="-69" r="103" fill="var(--brand-blue)"/>
      <!-- large decorative arcs -->
      <circle cx="740" cy="230" r="325" fill="none" stroke="var(--navy-mid)" stroke-width="22" opacity="0.55"/>
      <path d="M515 95 A250 250 0 0 1 650 5" fill="none" stroke="#244a8a" stroke-width="16" stroke-linecap="round"/>
      <circle cx="704" cy="198" r="160" fill="none" stroke="var(--ring-blue)" stroke-width="20"/>
      <!-- photo area -->
      <circle cx="704" cy="198" r="138" fill="url(#photoFill)" role="img" aria-label="Photo of a smiling caregiver in a white coat with her hands on the shoulders of a seated elderly woman"/>
      <!-- call circle -->
      <circle cx="490" cy="362" r="110" fill="none" stroke="var(--white)" stroke-width="1"/>
      <circle cx="490" cy="362" r="104" fill="var(--brand-blue)"/>
      <!-- dot grids -->
      <g fill="var(--white)">
        <circle cx="266" cy="53" r="1.6"/><circle cx="280" cy="53" r="1.6"/><circle cx="294" cy="53" r="1.6"/><circle cx="307" cy="53" r="1.6"/>
        <circle cx="266" cy="66" r="1.6"/><circle cx="280" cy="66" r="1.6"/><circle cx="294" cy="66" r="1.6"/><circle cx="307" cy="66" r="1.6"/>
        <circle cx="818" cy="321" r="1.6"/><circle cx="832" cy="321" r="1.6"/><circle cx="846" cy="321" r="1.6"/><circle cx="859" cy="321" r="1.6"/>
        <circle cx="818" cy="334" r="1.6"/><circle cx="832" cy="334" r="1.6"/><circle cx="846" cy="334" r="1.6"/><circle cx="859" cy="334" r="1.6"/>
      </g>
      <!-- tagline slash -->
      <polygon points="323,248 332,248 320,288 311,288" fill="var(--bright-cyan)"/>
    </svg>

    <div class="brand">
      <span class="brand-dot"></span>
      <span class="brand-name">Willow Hearth Caregivers</span>
    </div>

    <h1 class="headline">Let our family<br>take care of yours</h1>

    <div class="tagline-band"></div>
    <p class="tagline-text">It pays to care!</p>

    <p class="benefit">Eligible participants receive up to<br><strong>$15,000 a year,</strong> Tax Free.</p>

    <div class="call">
      <p class="call-label">Call us</p>
      <p class="call-number">(800)555-0142</p>
    </div>
  </section>
</body>
</html>
```